Create a webpage for TradeRefundo

TradeRefundo.com is a new forex rebate site we wish to launch in parallel to our sister site payoutlegion.com

Were looking for a webpage with a modern, clean, corporate professional feel, that shows we are a reliable trustworthy company.

Our company offers commission to its registered users based on the volume of trading activity. Essentially they receive a payment everytime they transact irrespective of whether that trade makes money or loses money.

Blue and green are the colours we have decided on so but we are still open to other colour schemes as long as they have a refreshing clean and smart appearance.

Target Market(s)

Online retail forex traders

Industry/Entity Type

Trade

Requirements
Must have
• We are not looking for many pages but at a minimum the payout legion.com website can guide you.

Another site of interest;
CoinReturn Trades

```html
<!DOCTYPE html>
<html lang="en">
<head>
<meta charset="utf-8">
<title>TradeRefundo</title>
<link href="https://fonts.googleapis.com/css2?family=Arimo:wght@400;700&display=swap" rel="stylesheet">
<style>
:root{
  --bg-dark:#2a2a2a;
  --page:#ffffff;
  --green:#1f8f3a;
  --green-dark:#0f5a22;
  --blue:#0d5aa0;
  --text-blue:#1e5fa8;
  --title-green:#2a8a30;
  --muted:#888;
  --ink:#222;
  --red:#cc1f1f;
}
*{box-sizing:border-box;margin:0;padding:0}
html,body{width:758px;height:1200px;overflow:hidden}
body{
  font-family:"Arimo",Arial,sans-serif;
  background:repeating-linear-gradient(135deg,#2f2f2f 0 3px,#262626 3px 6px);
  position:relative;color:var(--ink);
}
.page{position:absolute;left:69px;top:0;width:592px;height:1200px;background:var(--page)}
.abs{position:absolute}

/* header */
.brand{left:4px;top:6px;display:flex;align-items:center;gap:5px;font-weight:700;font-size:13px;color:var(--green-dark)}
.brand .mark{width:16px;height:16px;background:var(--green)}
.topbar{left:222px;top:17px;width:370px;height:20px;background:var(--blue);border-radius:4px;display:flex;align-items:center;gap:6px;padding:0 4px;font-size:8px;color:#fff;white-space:nowrap}
.btn-open{background:#2aa148;border-radius:3px;padding:3px 7px;font-weight:700}
.btn-login{background:#6d7f93;border-radius:3px;padding:3px 7px}
.search{margin-left:auto;background:#fff;color:#777;border-radius:3px;width:95px;height:13px;font-size:7px;line-height:9px;padding:2px 4px;overflow:hidden;white-space:nowrap}
.nav{left:0;top:50px;width:592px;height:20px;background:linear-gradient(#2ea045,#147a2c);display:flex;font-size:8px;color:#fff;align-items:center;white-space:nowrap}
.nav .home{width:24px;height:20px;background:#111;display:flex;align-items:center;justify-content:center}
.nav span.item{padding:0 13px;border-right:1px solid #4fb864;line-height:20px}

/* slider */
.slider{left:0;top:76px;width:592px;height:276px;background:linear-gradient(180deg,#0b0b0b,#000 60%,#101810)}
.dots{left:274px;top:327px;display:flex;gap:4px;align-items:center}
.dots i{width:10px;height:10px;border-radius:50%;background:#fff;display:block}
.dots i.on{background:#1e6fc0}

/* heads */
.head{background:var(--blue);color:#fff;font-size:11px;padding:3px 5px;border-radius:2px 2px 0 0;height:18px;white-space:nowrap}
.news-list{left:1px;top:378px;width:126px}
.news-list div{background:var(--green);color:#fff;font-size:7.5px;height:14px;line-height:14px;padding-left:3px;margin-bottom:1.5px;white-space:nowrap}
.brokers{left:136px;top:377px;width:455px;height:116px;border:2px solid #000}
.broker{position:absolute;font-size:13px;font-weight:700;color:#333;display:flex;align-items:center;gap:4px;white-space:nowrap}
.broker b{width:9px;height:9px;background:var(--green);display:block}

/* articles */
.photo{border:1px solid #333}
.art-title{font-size:15px;color:var(--title-green);white-space:nowrap}
.art-text{font-size:7.6px;line-height:11.3px;color:var(--text-blue);width:240px}
.more{background:var(--blue);color:#fff;font-size:7px;padding:2px 5px;border-radius:2px;white-space:nowrap}

/* quotes */
.panel{border:1px solid #ccc}
.quotes{font-size:6px}
.quotes tr td{height:8.4px;padding:0 3px}
.quotes tr:nth-child(odd){background:#f2f2f2}
.up{color:var(--green)} .dn{color:var(--red)}
.analysis a{display:block;color:var(--text-blue);font-size:9px;line-height:11px;text-decoration:none}
.analysis small{display:block;color:var(--muted);font-size:6.5px;margin:10px 0 10px}
.analysis .item{border-bottom:1px solid #ddd;padding:5px 4px 0}

/* features */
.feat h3{font-size:10px;font-weight:400;color:var(--title-green);margin:0 0 6px 24px;white-space:nowrap}
.feat p{font-size:7.6px;line-height:11px;color:var(--text-blue);width:118px;margin-left:20px}
.feat svg{position:absolute;left:0;top:-2px}

/* footer */
.footer{left:0;top:1083px;width:592px;height:117px;background:linear-gradient(#1f8a36,#0c5a20 55%,#083d15)}
.fcol{position:absolute;top:13px;color:#fff;font-size:7.2px;white-space:nowrap}
.fcol h4{font-size:8.5px;font-weight:400;margin-bottom:9px}
.fcol div{margin-bottom:5.5px}
.legal{left:8px;top:103px;display:flex;font-size:7px;color:#fff;white-space:nowrap}
.legal span{padding:0 8px;border-right:1px solid #bbb;text-decoration:underline}
.legal span:last-child{border:none}
.social{right:8px;top:97px;display:flex;align-items:center;gap:3px;color:#fff;font-size:9px;white-space:nowrap}
.social i{width:16px;height:16px;border-radius:50%;background:#2d73c9;display:block}
</style>
</head>
<body>
<div class="page">
  <div class="abs brand"><span class="mark"></span>TradeRefundo</div>
  <div class="abs topbar">
    <span class="btn-open">OPEN ACCOUNT</span><span class="btn-login">ACCOUNT LOGIN</span>
    <span>LIVE CHAT</span><span>ENG ▾</span>
    <span class="search">Search TradeRefundo...</span>
  </div>
  <nav class="abs nav">
    <span class="home"><svg width="11" height="10" viewBox="0 0 11 10"><path d="M5.5 0 11 5H9v5H6.5V7h-2v3H2V5H0z" fill="#fff"/></svg></span>
    <span class="item">FAQS ▾</span><span class="item">HOW IT WORKS ▾</span><span class="item">COMARE BROKERS ▾</span><span class="item">PRODUCTS ▾</span><span class="item">PROMOTION ▾</span><span class="item">BLOG ▾</span><span class="item" style="border:none">CONTACT US</span>
  </nav>

  <div class="abs slider" role="img" aria-label="Trading platform screen with live price chart and indicator grid"></div>
  <svg class="abs" style="left:0;top:76px" width="592" height="140"><polyline fill="none" stroke="#2fae3c" stroke-width="1" points="10,120 60,112 110,100 160,105 200,92 240,95 290,60 310,30 360,25 400,35 450,40 500,30 560,22 590,15"/></svg>
  <div class="abs dots"><span style="color:#fff;font-size:14px">❮</span><i></i><i class="on"></i><i></i><i></i><span style="color:#fff;font-size:14px">❯</span></div>

  <div class="abs head" style="left:1px;top:357px;width:126px">Forex News</div>
  <div class="abs news-list">
    <div>Test FOREX NEWS NO 1</div><div>Test FOREX NEWS NO 2</div><div>Test FOREX NEWS NO 3</div><div>Test FOREX NEWS NO 4</div><div>Test FOREX NEWS NO 5</div><div>Test FOREX NEWS NO 5</div><div>Test FOREX NEWS NO 5</div><div>Test FOREX NEWS NO 5</div>
  </div>
  <div class="abs head" style="left:136px;top:357px;width:126px;border-radius:2px">Leading Brokers</div>
  <div class="abs brokers">
    <div class="broker" style="left:6px;top:10px"><b></b>BlazeMarkets</div>
    <div class="broker" style="left:176px;top:10px"><b></b>SwiftFX Hub</div>
    <div class="broker" style="left:320px;top:10px"><b></b>Clearline FX</div>
    <div class="broker" style="left:40px;top:47px"><b></b>Quadra Pips</div>
    <div class="broker" style="left:222px;top:47px"><b></b>SteelTrade</div>
    <div class="broker" style="left:360px;top:47px"><b></b>Pointwise</div>
    <div class="broker" style="left:8px;top:86px"><b></b>Pips4All</div>
    <div class="broker" style="left:186px;top:86px"><b></b>OpenLot</div>
    <div class="broker" style="left:330px;top:86px"><b></b>Northwind FX</div>
  </div>

  <div class="abs photo" style="left:2px;top:500px;width:182px;height:146px;background:radial-gradient(circle at 45% 45%,#d9a034,#6b4210 55%,#1a0e03)" role="img" aria-label="Pile of gold coins beside a gold pot"></div>
  <div class="abs art-title" style="left:192px;top:500px">Test forex news number 7</div>
  <p class="abs art-text" style="left:195px;top:527px">oo can benefit from our forex rebate programme by requesting to go under the Payout Legion Affiliate Programme, with the online broker you are currently using. You will not be required to do anything other than make the request and rest assured that you will not see any impact on your current trading conditions. Simply visit our 'Broker Partners' Page, find the broker you are currently using and follow the sign-up procedure to join our forex rebate programme...........</p>
  <span class="abs more" style="left:195px;top:634px">Read More »</span>

  <div class="abs photo" style="left:2px;top:676px;width:182px;height:161px;background:radial-gradient(circle at 50% 40%,#f2e4c4,#b08a52 55%,#5a3c1c)" role="img" aria-label="Golden key resting on a note reading success"></div>
  <div class="abs art-title" style="left:192px;top:674px">Test forex news number 5</div>
  <p class="abs art-text" style="left:195px;top:707px">oo can benefit from our forex rebate programme by requesting to go under the Payout Legion Affiliate Programme, with the online broker you are currently using. You will not be required to do anything other than make the request and rest assured that you will not see any impact on your current trading conditions. Simply visit our 'Broker Partners' Page, find the broker you are currently using and follow the sign-up procedure to join our forex rebate programme...........</p>
  <span class="abs more" style="left:195px;top:822px">Read More »</span>

  <div class="abs head" style="left:440px;top:499px;width:150px;font-size:12px;height:20px">Markets Quotes</div>
  <div class="abs panel" style="left:440px;top:519px;width:150px;height:215px">
    <svg width="148" height="46" viewBox="0 0 148 46"><g stroke="#ddd" stroke-width=".5"><line x1="20" y1="6" x2="125" y2="6"/><line x1="20" y1="16" x2="125" y2="16"/><line x1="20" y1="26" x2="125" y2="26"/><line x1="20" y1="36" x2="125" y2="36"/></g><polyline fill="none" stroke="#2a9a3a" stroke-width="1" points="20,32 35,28 50,26 62,20 75,14 88,10 100,12 112,9 125,11"/><g font-size="4.5" fill="#555"><text x="2" y="8">1.462</text><text x="2" y="18">1.461</text><text x="2" y="28">1.441</text><text x="2" y="38">1.430</text><text x="128" y="8">0.71%</text><text x="128" y="18">0.47%</text><text x="128" y="28">0.23%</text><text x="128" y="38">-0.01%</text><text x="20" y="44">22:15</text><text x="45" y="44">00:10</text><text x="68" y="44">02:05</text><text x="90" y="44">04:00</text><text x="112" y="44">05:55</text></g></svg>
    <table class="quotes" style="width:148px;border-collapse:collapse">
      <tr><td>EURUSD</td><td class="up">+0.45%</td><td class="up">1.4254</td><td>-</td></tr>
      <tr><td>GBPUSD</td><td class="dn">-0.54%</td><td>1.6257</td><td>-</td></tr>
      <tr><td>USDJPY</td><td class="dn">-0.79%</td><td class="dn">80.40</td><td>-</td></tr>
      <tr><td>USDCHF</td><td class="dn">-0.50%</td><td class="dn">0.8831</td><td>-</td></tr>
      <tr><td>EURGBP</td><td class="up">+1.00%</td><td>0.8766</td><td>-</td></tr>
      <tr><td>EURJPY</td><td class="dn">-0.37%</td><td class="dn">114.61</td><td>-</td></tr>
      <tr><td>GBPJPY</td><td class="dn">-1.32%</td><td class="dn">130.71</td><td>-</td></tr>
      <tr><td>USDMXN</td><td class="dn">-0.05%</td><td>11.6323</td><td>-</td></tr>
      <tr><td>EURDKK</td><td class="up">+0.02%</td><td>7.4548</td><td>-</td></tr>
      <tr><td>AUDUSD</td><td class="dn">-0.26%</td><td>1.0671</td><td>-</td></tr>
      <tr><td>USDCAD</td><td class="up">+0.03%</td><td>0.9622</td><td>-</td></tr>
      <tr><td>NZDUSD</td><td class="up">+0.60%</td><td>0.7936</td><td>-</td></tr>
      <tr><td>AUDCAD</td><td class="dn">-0.22%</td><td>1.0267</td><td>-</td></tr>
      <tr><td>EURCHF</td><td class="dn">-0.04%</td><td>1.2590</td><td>-</td></tr>
      <tr><td>GBPCHF</td><td class="dn">-1.04%</td><td class="dn">1.4358</td><td>-</td></tr>
      <tr><td>EURAUD</td><td class="up">+0.72%</td><td>1.3353</td><td>-</td></tr>
      <tr><td>CHFJPY</td><td class="dn">-0.27%</td><td>91.02</td><td>-</td></tr>
    </table>
  </div>

  <div class="abs head" style="left:440px;top:741px;width:150px;font-size:12px;height:20px">Market Analysis</div>
  <div class="abs panel analysis" style="left:440px;top:761px;width:150px;height:213px">
    <div class="item"><a>Australia labour market beter than expected but its far from a game change</a><small>December 11,2013 09:12:50 PM</small></div>
    <div class="item"><a>Australia labour market beter than expected</a><small>December 11,2013 09:12:50 PM</small></div>
    <div class="item" style="border:none"><a>US Oil (WTI) Rebuffed by 200-day sma near $98.65...$97.00 key support</a><small>December 11,2013 09:12:50 PM</small></div>
  </div>

  <div class="abs feat" style="left:10px;top:856px">
    <svg width="18" height="18" viewBox="0 0 18 18"><path d="M3 10V8a6 6 0 0 1 12 0v2" fill="none" stroke="#aaa" stroke-width="1.6"/><rect x="2" y="9" width="3" height="5" rx="1" fill="#aaa"/><rect x="13" y="9" width="3" height="5" rx="1" fill="#aaa"/></svg>
    <h3>24 hour Customer Suport</h3>
    <p>Simply visit our 'Broker Partners' Page, find the broker you are currently using and follow the sign-up procedure to join our forex rebate programme</p>
  </div>
  <div class="abs feat" style="left:214px;top:857px">
    <svg width="18" height="18" viewBox="0 0 18 18"><circle cx="12" cy="5" r="4" fill="#aaa"/><path d="M9 8 2 15l2 2M5 12l2 2" stroke="#aaa" stroke-width="2" fill="none"/></svg>
    <h3>Funds Safety</h3>
    <p>Simply visit our 'Broker Partners' Page, find the broker you are currently using and follow the sign-up procedure to join our forex rebate programme</p>
  </div>
  <div class="abs feat" style="left:10px;top:963px">
    <svg width="18" height="18" viewBox="0 0 18 18"><rect x="5" y="0" width="9" height="17" rx="2" fill="none" stroke="#5a8fcf" stroke-width="1.5"/><circle cx="9.5" cy="14" r="1" fill="#5a8fcf"/></svg>
    <h3>Mobile Trading</h3>
    <p>Simply visit our 'Broker Partners' Page, find the broker you are currently using and follow the sign-up procedure to join our forex rebate programme</p>
  </div>
  <div class="abs feat" style="left:214px;top:963px">
    <svg width="18" height="18" viewBox="0 0 18 18"><path d="M1 17h16" stroke="#aaa"/><rect x="2" y="10" width="3" height="7" fill="#bbb"/><rect x="7" y="7" width="3" height="10" fill="#bbb"/><rect x="12" y="4" width="3" height="13" fill="#bbb"/><path d="M2 8l5-4 4 2 5-5" stroke="#5a8fcf" fill="none"/></svg>
    <h3>Free resarch &amp; insight</h3>
    <p>Simply visit our 'Broker Partners' Page, find the broker you are currently using and follow the sign-up procedure to join our forex rebate programme</p>
  </div>

  <footer class="abs footer">
    <div class="fcol" style="left:7px"><h4>WHY US?</h4><div>Global Market</div><div>Pricing &amp; Execution</div><div>Trading Technology</div><div>Financial Strength</div></div>
    <div class="fcol" style="left:86px"><h4>FOREX &amp; CFDs</h4><div>Forex</div><div>Index CFDs</div><div>CommoditiyCDFs</div></div>
    <div class="fcol" style="left:185px"><h4>PLATFORMS</h4><div>FORTEXT TRADER</div><div>CHARTDESK 4</div><div>Prime-Forex ECN</div></div>
    <div class="fcol" style="left:280px"><h4>MARKET ANALYSIS</h4><div>FORTEXT TRADER</div><div>Index CFDs</div><div>Trading Technology</div><div>Global Market</div></div>
    <div class="fcol" style="left:403px"><h4>CRESTLINE CAPITAL</h4><div>Global Market</div><div>Index CFDs</div><div>Prime-Forex ECN</div><div>Forex</div></div>
    <div class="fcol" style="left:508px"><h4>INTERNATIONAL</h4><div>Global Market</div><div>CHARTDESK 4</div><div>Financial Strength</div></div>
    <div class="abs legal"><span>Risk Warning</span><span>Custom Agreement</span><span>Privacy Policy</span><span>Conflicts Policy</span><span>Order Execution Policy</span><span>Site Map</span></div>
    <div class="abs social">Follow Us On: <i></i><i></i><i style="background:#d64a36"></i></div>
  </footer>
</div>
</body>
</html>
```